Edible Insect Sticker packaging design

The successful designer for this product will be hired again for more packaging design products in this product range.
We are a company that manufactures edible insects and we have some new products coming out we ned packaging for. As you can imagine the stickers are very small 50mm x 50mm.
Each sticker design will be in a set  of 2 (one for the front and one for the back of the packaging).
The front will contain the weight of the product (in grams) as well as the name of the product and design.
The back will contain our company logo and info as well as NIP (Nutritional Information Panel), ingredient declaration, and 3-4 lines of information about how edible insects are great for the environment.
At this stage I would like the packaging to have a slightly environmental free, but still colourful and eye catching. I am open to any suggestions for the design though if you have some great ideas!
Must also contain the slogan (on front or back), "Are you Brave Enough?"
There are several products in the range, and would like the labels to be in a set. Basic lay out will be the same for each product, and the front sticker will be slightly different.
Products are
Zip-A-Dee Crumble- a fly shaped chocolate that contains coconut and fly pupae
Toasty Hoppers- 5 x roasted crickets
Nibbly Grublets- 5 x roasted mealworms
Cocoa Dipped Beasties- 5 x insects, chocolate coated in milk, white or dark chocolate. Insects include crickets, mealworms and fly pupae
Specific information (eg, NIP, ingredients etc) will be sent to chosen designer to add to the deisgn.
Attached is image of 3 products (Zip-A-Dee Crumble, roasted mealworms and roasted crickets) as well as logo. The chocolate coated bugs are the 2 types of roasted bugs pictured in the attachment coated in chocolate.

Updates
Design can be square or round 

Reason: Several designers have asked for an extension to submit new/ revised designs.

Reason: I have extended the deadline by one day to allow for revisions and new designs to be submitted.

Industry/Entity Type
It Company
Look and feel
Each slider illustrates characteristics of the customer's brand and the style your logo design should communicate.

```html
<!DOCTYPE html>
<html lang="en">
<head>
<meta charset="utf-8">
<title>Insect Snack Sticker Set</title>
<link rel="stylesheet" href="https://fonts.googleapis.com/css2?family=Ubuntu:wght@500;700&display=swap">
<style>
  :root {
    --backdrop: #2a2a2a;
    --orange: #f59c2a;
    --green: #a3c12f;
    --blue: #3aaec8;
    --red: #d42127;
    --ink: #ffffff;
  }
  * { margin: 0; padding: 0; box-sizing: border-box; }
  html, body { width: 1200px; height: 900px; overflow: hidden; }
  body {
    background: var(--backdrop);
    font-family: "Ubuntu", "Helvetica Neue", Arial, sans-serif;
    color: var(--ink);
    position: relative;
  }
  .sticker {
    position: absolute;
    width: 239px;
    height: 239px;
    border-radius: 16px;
    background: var(--tone);
    overflow: hidden;
  }
  .tone-orange { --tone: var(--orange); }
  .tone-green  { --tone: var(--green); }
  .tone-blue   { --tone: var(--blue); }
  .tone-red    { --tone: var(--red); }

  .col-1 { left: 86px; }
  .col-2 { left: 349px; }
  .col-3 { left: 612px; }
  .col-4 { left: 875px; }
  .front { top: 174px; }
  .back  { top: 485px; }

  /* faint insect pattern area */
  .bug-pattern {
    position: absolute;
    inset: 0;
    background:
      radial-gradient(circle at 80% 30%, rgba(0,0,0,0.08), transparent 55%),
      radial-gradient(circle at 30% 85%, rgba(0,0,0,0.07), transparent 45%);
  }

  .product-name {
    position: absolute;
    left: 24px;
    top: 12px;
    width: 200px;
    font-weight: 700;
    line-height: 0.95;
    letter-spacing: -0.5px;
    white-space: nowrap;
  }
  .product-name span { display: block; }
  .rule {
    position: absolute;
    left: 24px;
    top: 106px;
    width: 196px;
    height: 2px;
    background: var(--ink);
  }
  .contents {
    position: absolute;
    left: 24px;
    top: 113px;
    font-size: 13.5px;
    font-weight: 500;
    white-space: nowrap;
  }
  .weight-line {
    position: absolute;
    left: 24px;
    top: 130px;
    display: flex;
    align-items: center;
    gap: 6px;
  }
  .weight { font-size: 28px; font-weight: 700; letter-spacing: -0.5px; }
  .weight-divider { width: 2px; height: 20px; background: var(--ink); }
  .weight-note { font-size: 9px; font-weight: 700; line-height: 1; }

  .brave-badge {
    position: absolute;
    left: 22px;
    top: 168px;
    width: 74px;
    height: 64px;
  }
  .brave-badge p {
    position: absolute;
    left: 0; right: 0;
    top: 24px;
    text-align: center;
    font-size: 7.5px;
    font-weight: 700;
    line-height: 1.05;
  }

  .brand {
    position: absolute;
    right: 18px;
    bottom: 22px;
    display: flex;
    align-items: center;
    gap: 6px;
    font-size: 17px;
    font-weight: 700;
    line-height: 0.95;
    text-transform: uppercase;
    text-align: right;
  }
  .brand-dot {
    width: 12px; height: 12px;
    border-radius: 50%;
    background: var(--ink);
  }

  .panel-heading {
    position: absolute;
    font-size: 12px;
    font-weight: 700;
    line-height: 1;
    text-transform: uppercase;
  }
  .heading-nutrition { left: 17px; top: 19px; }
  .heading-info { left: 140px; top: 19px; }
  .heading-ingredients { left: 17px; top: 116px; }
  .code-box {
    position: absolute;
    left: 17px;
    top: 205px;
    width: 73px;
    height: 24px;
    border-radius: 6px;
    background: var(--ink);
  }
</style>
</head>
<body>

  <!-- Front stickers -->
  <section class="sticker front tone-orange col-1">
    <div class="bug-pattern" role="img" aria-label="Faint scattered insect silhouettes"></div>
    <h2 class="product-name"><span style="font-size:46px">nibbly</span><span style="font-size:35px">grublets</span></h2>
    <div class="rule"></div>
    <p class="contents">5 x roasted mealworms</p>
    <div class="weight-line"><span class="weight">25gr</span><span class="weight-divider"></span><span class="weight-note">Contains<br>Real Bugs</span></div>
    <div class="brave-badge"><svg width="74" height="64" viewBox="0 0 74 64"><path d="M37 3 L71 61 L3 61 Z" fill="none" stroke="#fff" stroke-width="3" stroke-linejoin="round"/></svg><p>ARE<br>YOU<br>BRAVE<br>ENOUGH?</p></div>
    <div class="brand"><span class="brand-dot"></span><span>Crawly<br>Pantry</span></div>
  </section>

  <section class="sticker front tone-green col-2">
    <div class="bug-pattern" role="img" aria-label="Faint scattered insect silhouettes"></div>
    <h2 class="product-name"><span style="font-size:38px">toasty</span><span style="font-size:50px">hoppers</span></h2>
    <div class="rule"></div>
    <p class="contents">5 x roasted crickets</p>
    <div class="weight-line"><span class="weight">25gr</span><span class="weight-divider"></span><span class="weight-note">Contains<br>Real Bugs</span></div>
    <div class="brave-badge"><svg width="74" height="64" viewBox="0 0 74 64"><path d="M37 3 L71 61 L3 61 Z" fill="none" stroke="#fff" stroke-width="3" stroke-linejoin="round"/></svg><p>ARE<br>YOU<br>BRAVE<br>ENOUGH?</p></div>
    <div class="brand"><span class="brand-dot"></span><span>Crawly<br>Pantry</span></div>
  </section>

  <section class="sticker front tone-blue col-3">
    <div class="bug-pattern" role="img" aria-label="Faint scattered insect silhouettes"></div>
    <h2 class="product-name"><span style="font-size:36px">zip-a-dee</span><span style="font-size:48px">crumble</span></h2>
    <div class="rule"></div>
    <p class="contents">coconut and fly pupae</p>
    <div class="weight-line"><span class="weight">25gr</span><span class="weight-divider"></span><span class="weight-note">Contains<br>Real Bugs</span></div>
    <div class="brave-badge"><svg width="74" height="64" viewBox="0 0 74 64"><path d="M37 3 L71 61 L3 61 Z" fill="none" stroke="#fff" stroke-width="3" stroke-linejoin="round"/></svg><p>ARE<br>YOU<br>BRAVE<br>ENOUGH?</p></div>
    <div class="brand"><span class="brand-dot"></span><span>Crawly<br>Pantry</span></div>
  </section>

  <section class="sticker front tone-red col-4">
    <div class="bug-pattern" role="img" aria-label="Faint scattered insect silhouettes"></div>
    <h2 class="product-name"><span style="font-size:30px">cocoa dipped</span><span style="font-size:48px">beasties</span></h2>
    <div class="rule"></div>
    <p class="contents">5 x insects chocolate coated</p>
    <div class="weight-line"><span class="weight">25gr</span><span class="weight-divider"></span><span class="weight-note">Contains<br>Real Bugs</span></div>
    <div class="brave-badge"><svg width="74" height="64" viewBox="0 0 74 64"><path d="M37 3 L71 61 L3 61 Z" fill="none" stroke="#fff" stroke-width="3" stroke-linejoin="round"/></svg><p>ARE<br>YOU<br>BRAVE<br>ENOUGH?</p></div>
    <div class="brand"><span class="brand-dot"></span><span>Crawly<br>Pantry</span></div>
  </section>

  <!-- Back stickers -->
  <section class="sticker back tone-orange col-1">
    <h3 class="panel-heading heading-nutrition">Nutritional<br>Facts:</h3>
    <h3 class="panel-heading heading-info">How eating<br>bugs:</h3>
    <h3 class="panel-heading heading-ingredients">Ingredients:</h3>
    <div class="code-box"></div>
    <div class="brand"><span class="brand-dot"></span><span>Crawly<br>Pantry</span></div>
  </section>

  <section class="sticker back tone-green col-2">
    <h3 class="panel-heading heading-nutrition">Nutritional<br>Facts:</h3>
    <h3 class="panel-heading heading-info">How eating<br>bugs:</h3>
    <h3 class="panel-heading heading-ingredients">Ingredients:</h3>
    <div class="code-box"></div>
    <div class="brand"><span class="brand-dot"></span><span>Crawly<br>Pantry</span></div>
  </section>

  <section class="sticker back tone-blue col-3">
    <h3 class="panel-heading heading-nutrition">Nutritional<br>Facts:</h3>
    <h3 class="panel-heading heading-info">How eating<br>bugs:</h3>
    <h3 class="panel-heading heading-ingredients">Ingredients:</h3>
    <div class="code-box"></div>
    <div class="brand"><span class="brand-dot"></span><span>Crawly<br>Pantry</span></div>
  </section>

  <section class="sticker back tone-red col-4">
    <h3 class="panel-heading heading-nutrition">Nutritional<br>Facts:</h3>
    <h3 class="panel-heading heading-info">How eating<br>bugs:</h3>
    <h3 class="panel-heading heading-ingredients">Ingredients:</h3>
    <div class="code-box"></div>
    <div class="brand"><span class="brand-dot"></span><span>Crawly<br>Pantry</span></div>
  </section>

</body>
</html>
```